Software allocation system needs a business card design

We need a business card designed for our software platform - www.tolvexa.com.au

At the moment the logo and website is all black and white, we are happy for suggestions on implementing some colour throughout either the logo or business card.

Industry/Entity Type

Software

Font styles to use
Sans Serif

Colors

Designer to choose colors to be used in the design.

```html
<!DOCTYPE html>
<html lang="en">
<head>
<meta charset="utf-8">
<title>Tolvexa Business Card</title>
<link rel="stylesheet" href="https://fonts.googleapis.com/css2?family=Questrial&display=swap">
<style>
  :root {
    --page-bg: #e6e8ea;
    --card-white: #f4f4f4;
    --teal: #0f8a92;
    --navy: #0b2d52;
    --ink: #2c3e55;
    --ink-soft: #4a5a6c;
    --brand: #17607a;
    --faint-grey: #e2e2e2;
  }
  * { box-sizing: border-box; margin: 0; padding: 0; }
  html, body { width: 1200px; height: 900px; overflow: hidden; }
  body {
    background: var(--page-bg);
    font-family: "Questrial", "Century Gothic", sans-serif;
    display: flex;
    flex-direction: column;
    align-items: center;
    justify-content: center;
    gap: 48px;
  }
  .card {
    position: relative;
    width: 630px;
    height: 360px;
    overflow: hidden;
    box-shadow: 0 6px 18px rgba(0,0,0,0.15);
  }
  /* Front */
  .card-front {
    background: linear-gradient(160deg, var(--teal) 0%, #0b5a77 50%, var(--navy) 100%);
  }
  .card-front .deco-ring {
    position: absolute;
    left: 120px;
    top: -60px;
    width: 240px;
    height: 240px;
    border-radius: 50%;
    border: 34px solid rgba(255,255,255,0.09);
  }
  .card-front .wordmark {
    position: absolute;
    right: 70px;
    bottom: 70px;
    color: #ffffff;
    font-size: 34px;
    letter-spacing: 5px;
  }
  /* Back */
  .card-back { background: var(--card-white); }
  .card-back .deco-ring {
    position: absolute;
    left: 250px;
    top: 210px;
    width: 250px;
    height: 250px;
    border-radius: 50%;
    border: 44px solid var(--faint-grey);
  }
  .identity {
    position: absolute;
    left: 56px;
    top: 48px;
    color: var(--ink);
  }
  .identity .person-name {
    font-size: 13px;
    letter-spacing: 2.5px;
    text-transform: uppercase;
  }
  .identity .person-role {
    font-size: 11px;
    letter-spacing: 1.5px;
    color: var(--brand);
    margin-top: 4px;
  }
  .identity .address {
    font-size: 11.5px;
    letter-spacing: 1px;
    color: var(--ink-soft);
    margin-top: 14px;
  }
  .contact-list {
    position: absolute;
    left: 56px;
    top: 150px;
    list-style: none;
    color: var(--ink-soft);
    font-size: 11.5px;
    letter-spacing: 1.2px;
  }
  .contact-list li {
    display: flex;
    align-items: center;
    gap: 10px;
    height: 20px;
  }
  .contact-list svg { width: 11px; height: 11px; fill: none; stroke: var(--brand); stroke-width: 1.6; }
  .card-back .wordmark {
    position: absolute;
    right: 70px;
    top: 150px;
    color: var(--brand);
    font-size: 36px;
    letter-spacing: 5px;
  }
</style>
</head>
<body>
  <section class="card card-front" aria-label="Card front">
    <div class="deco-ring"></div>
    <div class="wordmark">TOLVEXA</div>
  </section>

  <section class="card card-back" aria-label="Card back">
    <div class="deco-ring"></div>
    <div class="identity">
      <p class="person-name">Lukas Brenner</p>
      <p class="person-role">CEO</p>
      <p class="address">Lindenweg 7, 5401 Baden, Switzerland</p>
    </div>
    <ul class="contact-list">
      <li>
        <svg viewBox="0 0 12 12"><path d="M2 1.5h2.5l1 2.5-1.3 1a6 6 0 0 0 2.8 2.8l1-1.3 2.5 1V10a1 1 0 0 1-1 1A9 9 0 0 1 1 2.5a1 1 0 0 1 1-1z"/></svg>
        <span>+41 56 000 12 34</span>
      </li>
      <li>
        <svg viewBox="0 0 12 12"><rect x="3" y="1" width="6" height="10" rx="1"/><path d="M5.5 9h1"/></svg>
        <span>+41 79 000 56 78</span>
      </li>
      <li>
        <svg viewBox="0 0 12 12"><rect x="1" y="2.5" width="10" height="7" rx="0.5"/><path d="M1 3l5 3.5L11 3"/></svg>
        <span>lukas.brenner@tolvexa.ch</span>
      </li>
      <li>
        <svg viewBox="0 0 12 12"><circle cx="6" cy="6" r="4.8"/><path d="M1.2 6h9.6M6 1.2c-2.4 2.6-2.4 7 0 9.6M6 1.2c2.4 2.6 2.4 7 0 9.6"/></svg>
        <span>www.tolvexa.com.au</span>
      </li>
    </ul>
    <div class="wordmark">TOLVEXA</div>
  </section>
</body>
</html>
```